Stone Over Tide - Stationery Design Project

Hi everyone,

We need a business card and a stationary set designed for a new corporate video production company based in Sydney, 'Stone Over Tide'.

The name refers to the mythological 'phoenix' so we would like to see designs that are appropriate to both the name and to a creative film company. The key thing is, we need to appear fresh and creative while maintaining professionalism.

We would like to stick with dark colors for the basis of the card. One idea that came up was obsidian/volcanic rock with the logo cracking through to reveal lava or something fire like. This is just one idea that has come up, but we are of course open to others and would love to see what people can come up with. Extensive use of flames/fire imagery is not really what we are after.

Also, cinematic as opposed to corporate is preferable.

**** UPDATE ****
When I hand over the card to a prospective client, I want them to feel like they are receiving an obsidian plate with inscriptions in it (ie the phoenix). Looking for something elemental and rigid to contrast and complement the graceful lines of the logo.

Designs we require:
- Business card
(We would like a business card that makes use of some of the more premium business card printing options, such as foil stamping, embossing/debossing, painted edges, spot UV etc. Doesnt have to use all these things, only what you feel works, but we are looking for a business card that stands out and is memorable and these nice touches have that effect. For an example of what is possible, check out "http://www.velvetprintery.net/base/category/business-card-gallery/".)

- Letter head
- With compliments slip
- Display folder

COPMPANY DETAILS:
ABN: 62 738 294 019
Company Address: 7/18-20 Kell St, Marbury NSW 2058
Name: Rex M. Dunleavy
Producer: Producer
Contact Number: 0412 539 204
email: rex@stoneovertide.com
website: www.stoneovertide.com

ABOUT THE PHOENIX:
The phoenix is a musical bird from mythology, known for its long fancy tail and small plume on the top of its head. They are elegant and graceful and symbolize immortality, endurance and strength, believed to live for 5 centuries before they were reborn from their ashes.
Updates

Hi everyone,

We have just updated the design brief to include business contact information, website etc. should anyone require it for their designs.

Thanks

Rex

Target Market(s)

Other creative businesses and marketing firms.

Industry/Entity Type

Printing

Requirements
Must have
• Basic printing requirements:
- CMYK colour space
- 300dpi resolution
- Color bleed/crop marks etc to allow for trimming where necessary
- Source files upon handover
Should not have
• Overuse of fire/flame imagery

```html
<!DOCTYPE html>
<html lang="en">
<head>
<meta charset="utf-8">
<title>Stone Over Tide – Business Card</title>
<link rel="stylesheet" href="https://fonts.googleapis.com/css2?family=Open+Sans:wght@300;400;600;700&display=swap">
<style>
  :root {
    --canvas: #2a2522;
    --obsidian-deep: #030304;
    --obsidian-mid: #121214;
    --obsidian-sheen: rgba(255, 255, 255, 0.07);
    --signal-red: #f41a0a;
    --rule-white: #ffffff;
    --ink-white: #ffffff;
    --ink-soft: #d9d9d9;
    --divider: #6a6a6a;
  }
  * { box-sizing: border-box; margin: 0; padding: 0; }
  html, body {
    width: 1200px; height: 758px; overflow: hidden;
    background: var(--canvas);
    font-family: "Open Sans", Arial, sans-serif;
  }
  .stage {
    position: relative; width: 1200px; height: 758px;
    display: flex; align-items: center; justify-content: center; gap: 44px;
  }
  .card {
    position: relative; width: 540px; height: 308px; overflow: hidden;
    color: var(--ink-white);
    background:
      linear-gradient(118deg, transparent 30%, var(--obsidian-sheen) 42%, transparent 52%),
      radial-gradient(ellipse at 30% 20%, var(--obsidian-mid), var(--obsidian-deep) 70%);
    box-shadow: inset 0 0 0 1px rgba(255, 255, 255, 0.06);
  }

  /* Front */
  .band { position: absolute; left: 0; right: 0; background: var(--signal-red); }
  .band--top { top: 0; height: 34px; border-bottom: 3px solid var(--rule-white); }
  .band--bottom {
    bottom: 0; height: 46px; border-top: 3px solid var(--rule-white);
    display: flex; align-items: center; justify-content: center;
    font-size: 13px; letter-spacing: 0.6px;
  }
  .band--top::after, .band--bottom::before {
    content: ""; position: absolute; left: 0; right: 0; height: 3px; background: var(--obsidian-deep);
  }
  .band--top::after { bottom: -6px; }
  .band--bottom::before { top: -6px; }

  .front-body {
    position: absolute; top: 40px; bottom: 52px; left: 0; right: 0;
    display: flex; flex-direction: column; align-items: center;
  }
  .brand-mark {
    width: 30px; height: 30px; border-radius: 50%;
    background: var(--signal-red); margin-top: 22px;
  }
  .brand-name {
    margin-top: 16px; font-size: 11px; font-weight: 400;
    letter-spacing: 7px; text-transform: uppercase;
  }
  .person {
    margin-top: 12px; font-size: 19px; font-weight: 700; letter-spacing: 0.4px;
  }
  .person .title { font-weight: 400; }
  .divider {
    width: 250px; height: 2px; margin-top: 7px;
    background: linear-gradient(90deg, transparent, var(--divider) 40%, var(--divider) 60%, transparent);
  }
  .contact-row {
    display: flex; gap: 18px; margin-top: 9px; font-size: 12.5px; color: var(--ink-soft);
    white-space: nowrap;
  }
  .contact-row--web { margin-top: 4px; }
  .contact-item { display: inline-flex; align-items: center; gap: 5px; }
  .contact-item svg { width: 11px; height: 11px; fill: var(--ink-soft); }
  .contact-item .stroke { fill: none; stroke: var(--ink-soft); }

  /* Back */
  .back { display: flex; align-items: center; justify-content: center; gap: 18px; }
  .back .brand-mark {
    width: 110px; height: 110px; margin: 0; background: var(--ink-white);
  }
  .back-copy { display: flex; flex-direction: column; gap: 10px; }
  .back-name { font-size: 24px; font-weight: 400; letter-spacing: 3px; text-transform: uppercase; }
  .back-web { font-size: 19px; letter-spacing: 1.6px; }
</style>
</head>
<body>
<main class="stage">

  <section class="card front" aria-label="Business card front">
    <div class="band band--top"></div>
    <div class="front-body">
      <span class="brand-mark" aria-hidden="true"></span>
      <p class="brand-name">Stone Over Tide</p>
      <p class="person">Rex M. Dunleavy, <span class="title">Producer</span></p>
      <span class="divider"></span>
      <p class="contact-row">
        <span class="contact-item">
          <svg viewBox="0 0 12 12" aria-hidden="true"><path d="M2.5 0.8l2 2.2-1 1.3c.7 1.6 2 2.9 3.6 3.6l1.3-1 2.2 2-1 2C5.4 10.7 1.3 6.6 0.5 2z"/></svg>0412 539 204
        </span>
        <span class="contact-item">
          <svg viewBox="0 0 12 12" aria-hidden="true"><rect x="3" y="0.5" width="6" height="4"/><rect x="0.5" y="5" width="11" height="5" rx="1"/></svg>ABN 62 738 294 019
        </span>
        <span class="contact-item">
          <svg viewBox="0 0 12 12" aria-hidden="true"><path class="stroke" stroke-width="1.3" d="M0.5 2.5h11v7h-11z M0.5 2.5l5.5 4 5.5-4"/></svg>rex@stoneovertide.com
        </span>
      </p>
      <p class="contact-row contact-row--web">
        <span class="contact-item">
          <svg viewBox="0 0 12 12" aria-hidden="true"><circle class="stroke" stroke-width="1.2" cx="6" cy="6" r="5"/><path class="stroke" stroke-width="1" d="M1 6h10M6 1c-2.5 3-2.5 7 0 10M6 1c2.5 3 2.5 7 0 10"/></svg>www.stoneovertide.com
        </span>
      </p>
    </div>
    <div class="band band--bottom">7/18-20 Kell St, Marbury NSW 2058</div>
  </section>

  <section class="card back" aria-label="Business card back">
    <span class="brand-mark" aria-hidden="true"></span>
    <div class="back-copy">
      <p class="back-name">Stone Over Tide</p>
      <p class="back-web">www.stoneovertide.com</p>
    </div>
  </section>

</main>
</body>
</html>
```